Australian Legal Practice would like a Web Design

I need a web design for a newly established law practice operating as Brindell Legal.

I would like the business to have an internet presence (via a website) essentially for the purpose of marketing and advertising. As the business grows (hopefully) I may be interested in providing general legal information as a means of establishing goodwill in the community and a easy and user friends contact method through the website.

The essence of the business is personal legal service based on local knowledge and therefore i want the website to present a picture of friendly professionalism, but mostly i want people who to be able to find the contact details of the business

I would like to have a map of the office location, and photos of the front of the office, the staff (me at the moment) and picture of law themed items and featuring the Brindell Legal logo.

The areas of law which Brindell Legal practises in are as follows:

commercial law
business sale and purchases
leases
conveyancing and property law
wills and estates
powers of attorney
general legal advice
succession planning
Updates

Target Market(s)

Potential and existing clients of the firm
Other law firms
Associated stakeholders, i.e. Banks and real estate agents

Industry/Entity Type

Law Firm

Coding

Coded - Design and coding required

Number of Pages Required

2 page

Font styles to use
Sans Serif

Colors
85acd3
33a6d7
0456a4

Requirements
Must have
• Brindell Legal logo
• Map of the office location
• Picture of Ross Kedwick (principal solicitor)
• Picture of the office
• Areas of Practice
• Address of office
• email address: ross.kedwick@brindelllegal-example.com.au
• Physical address: 17 Pellow Road, Hamilton VIC 3300
• Phone number: (03) 5598 4731
• Facsimile number: (03) 5598 4706
• Space for a brief description of the firm and its competitive advantage
• Bar Guild Logo
• Links to the Bar Guild of Victoria
• Link to the practitioner oversight Council
Nice to have
• coded to wordpress format

```html
<!DOCTYPE html>
<html lang="en">
<head>
<meta charset="utf-8">
<title>Brindell Legal</title>
<link href="https://fonts.googleapis.com/css2?family=Open+Sans:wght@300;400;600;700&display=swap" rel="stylesheet">
<style>
:root{
  --navy:#0a2a9c;
  --blue:#0b3cc4;
  --royal:#0456a4;
  --sky:#33a6d7;
  --pale:#85acd3;
  --ink:#2b2b2b;
  --grey:#6b6b6b;
  --light:#eef0f3;
  --white:#ffffff;
}
*{box-sizing:border-box;margin:0;padding:0}
html,body{width:1200px;height:2208px;overflow:hidden}
body{font-family:"Open Sans",Arial,sans-serif;color:var(--ink);background:var(--white);position:relative}
.site-header{position:absolute;top:0;left:0;width:1200px;height:72px;background:var(--white);z-index:3}
.brand-small{position:absolute;left:200px;top:20px;font-weight:700;font-size:24px;color:var(--navy);letter-spacing:1px}
.main-nav{position:absolute;left:420px;top:0;display:flex;height:72px}
.main-nav a{display:block;padding:0 20px;line-height:72px;font-size:13px;color:var(--grey);text-decoration:none;font-weight:600;letter-spacing:1px}
.main-nav a.active{background:var(--blue);color:var(--white)}
.hero{position:absolute;top:72px;left:0;width:1200px;height:400px;background:linear-gradient(90deg,var(--navy),var(--blue));overflow:hidden}
.hero-photo{position:absolute;left:640px;top:0;width:340px;height:400px;background:linear-gradient(180deg,#4f6fbf,#1a2f6e)}
.hero-brand{position:absolute;left:260px;top:150px;color:var(--white);font-size:42px;font-weight:700;letter-spacing:2px;white-space:nowrap}
.hero-tagline{position:absolute;left:180px;top:228px;color:var(--white);font-size:14px;font-weight:600;letter-spacing:.5px;white-space:nowrap}
.hero-text{position:absolute;left:180px;top:256px;width:420px;color:#d6defa;font-size:12px;line-height:18px}
.about{position:absolute;top:480px;left:0;width:1200px;height:320px}
.about-photo{position:absolute;left:0;top:0;width:560px;height:320px;background:linear-gradient(135deg,#f4f4f4,#b9bec4)}
.about-body{position:absolute;left:600px;top:60px;width:560px;text-align:center}
.section-title{font-size:26px;font-weight:600;letter-spacing:2px;color:var(--navy)}
.about-sub{font-size:12px;color:var(--grey);letter-spacing:1px;margin:6px 0 12px}
.about p{font-size:12px;line-height:18px;color:var(--grey);text-align:left}
.about-quote{font-size:22px;font-weight:700;color:var(--navy);margin:16px 0 10px;letter-spacing:1px}
.services{position:absolute;top:800px;left:0;width:1200px;height:360px;background:linear-gradient(180deg,var(--blue),var(--navy));color:var(--white);text-align:center}
.services .section-title{color:var(--white);margin-top:48px}
.service-list{display:flex;justify-content:center;gap:60px;margin-top:40px}
.service{width:200px}
.service svg{width:70px;height:70px}
.service h3{font-size:14px;font-weight:600;margin:26px 0 10px;letter-spacing:1px}
.service p{font-size:11px;line-height:16px;color:#cfd8fb}
.practices{position:absolute;top:1160px;left:0;width:1200px;height:420px}
.practice-list{position:absolute;left:200px;top:70px;width:360px;text-align:center}
.practice-list ul{list-style:none;margin-top:24px}
.practice-list li{font-size:15px;line-height:27px;color:var(--ink);letter-spacing:.5px}
.gavel-photo{position:absolute;left:600px;top:0;width:600px;height:420px;background:linear-gradient(160deg,#f1ede8,#8a5a32 70%,#5b351a)}
.contact{position:absolute;top:1580px;left:0;width:1200px;height:500px;background:linear-gradient(90deg,var(--white) 60%,var(--light))}
.contact .section-title{position:absolute;top:36px;width:100%;text-align:center}
.contact-form{position:absolute;left:220px;top:120px;width:400px}
.contact-form label{display:block;font-size:11px;color:var(--grey);margin-bottom:4px}
.field{height:30px;border:1px solid #cfd3d9;background:var(--white);margin-bottom:10px}
.field.tall{height:110px}
.form-foot{display:flex;justify-content:space-between;align-items:center;font-size:10px;color:var(--grey)}
.send{background:var(--blue);color:var(--white);font-size:11px;padding:8px 22px;font-weight:600}
.map{position:absolute;left:650px;top:120px;width:320px;height:160px;background:linear-gradient(135deg,#e6e9ee,#d3dae3)}
.contact-note{position:absolute;left:650px;top:292px;width:320px;font-size:10px;line-height:15px;color:var(--grey)}
.contact-items{position:absolute;left:650px;top:340px;width:340px;display:flex;justify-content:space-between;font-size:9px;color:var(--grey);text-align:center}
.contact-items div{width:82px}
.contact-items svg{width:22px;height:22px;display:block;margin:0 auto 4px}
.site-footer{position:absolute;top:2124px;left:0;width:1200px;height:84px;background:var(--navy);color:var(--white)}
.social{position:absolute;left:200px;top:20px;display:flex;gap:12px}
.social span{width:16px;height:16px;border-radius:50%;background:var(--white);display:block}
.copyright{position:absolute;left:200px;top:48px;font-size:10px;color:#c8d2f8}
.badges{position:absolute;left:800px;top:18px;display:flex;gap:14px}
.badge{width:48px;height:48px;background:var(--white)}
.badge.wide{width:80px}
</style>
</head>
<body>
<header class="site-header">
  <div class="brand-small">BRINDELL Legal</div>
  <nav class="main-nav">
    <a class="active" href="#">HOME</a><a href="#">ABOUT US</a><a href="#">SERVICES</a><a href="#">CONTACT</a>
  </nav>
</header>

<section class="hero">
  <div class="hero-photo" role="img" aria-label="Portrait of Ross Kedwick, principal solicitor, in a dark suit"></div>
  <div class="hero-brand">BRINDELL Legal</div>
  <div class="hero-tagline">WE OFFER OUR CLIENTS ONLY EXPERT LEGAL ADVICE</div>
  <p class="hero-text">Local solicitors providing friendly, practical advice to individuals, families and businesses across Hamilton and the Western District. We take time to listen, explain your options in plain language and guide you clearly through every step of your matter.</p>
</section>

<section class="about">
  <div class="about-photo" role="img" aria-label="Bright modern office interior with reception seating"></div>
  <div class="about-body">
    <h2 class="section-title">ABOUT US</h2>
    <div class="about-sub">LOREM IPSUM PASSAGES, AND MORE RECENTLY</div>
    <p>Brindell Legal is a newly established practice built on local knowledge and personal service. Our principal solicitor works directly with every client, so you always know who is handling your matter and how it is progressing.</p>
    <div class="about-quote">"IT WAS POPULARISED IN THE 1960S"</div>
    <p>We advise on property, business and estate matters with clear fees and prompt replies. Being part of the Hamilton community means we understand local needs and can offer advice that fits your circumstances.</p>
  </div>
</section>

<section class="services">
  <h2 class="section-title">SERVICES</h2>
  <div class="service-list">
    <div class="service">
      <svg viewBox="0 0 70 70" fill="none" stroke="#fff" stroke-width="3"><path d="M35 8v50M18 58h34M12 20h46M12 20l-8 18h16zM58 20l-8 18h16z"/></svg>
      <h3>CRIMINAL DEFENCE</h3>
      <p>Clear guidance and steady support when you face charges or court appearances.</p>
    </div>
    <div class="service">
      <svg viewBox="0 0 70 70" fill="none" stroke="#fff" stroke-width="3"><rect x="4" y="4" width="62" height="62" rx="14"/><circle cx="27" cy="28" r="8"/><circle cx="45" cy="28" r="8"/><path d="M13 54c2-10 26-10 28 0M31 54c2-10 26-10 28 0"/></svg>
      <h3>CIVIL LITIGATION</h3>
      <p>Practical advice on disputes, negotiation and resolving matters without delay.</p>
    </div>
    <div class="service">
      <svg viewBox="0 0 70 70" fill="none" stroke="#fff" stroke-width="3"><path d="M6 34L35 8l29 26M14 28v34h42V28M29 62V44h12v18"/></svg>
      <h3>ESTATE PLANNING</h3>
      <p>Wills, powers of attorney and succession plans to protect your family's future.</p>
    </div>
  </div>
</section>

<section class="practices">
  <div class="practice-list">
    <h2 class="section-title">PRACTICES</h2>
    <ul>
      <li>COMMERCIAL LAW</li>
      <li>BUSINESS SALE AND PURCHASES</li>
      <li>LEASES</li>
      <li>CONVEYANCING AND PROPERTY LAW</li>
      <li>WILLS AND ESTATES</li>
      <li>POWERS OF ATTORNEY</li>
      <li>GENERAL LEGAL ADVICE</li>
      <li>SUCCESSION PLANNING</li>
    </ul>
  </div>
  <div class="gavel-photo" role="img" aria-label="Wooden judge's gavel resting on a desk"></div>
</section>

<section class="contact">
  <h2 class="section-title">CONTACT</h2>
  <div class="contact-form">
    <label>Name</label><div class="field"></div>
    <label>Email</label><div class="field"></div>
    <label>Subject</label><div class="field"></div>
    <label>Message</label><div class="field tall"></div>
    <div class="form-foot"><span>* All fields are required</span><span class="send">SEND</span></div>
  </div>
  <div class="map" role="img" aria-label="Street map showing the office at 17 Pellow Road, Hamilton"></div>
  <p class="contact-note">Call, email or visit our Hamilton office. Appointments are available on weekdays and we aim to reply to every enquiry within one business day.</p>
  <div class="contact-items">
    <div><svg viewBox="0 0 22 22" fill="#0a2a9c"><path d="M5 2l4 4-2 3c1 3 3 5 6 6l3-2 4 4-3 3C9 20 2 13 2 5z"/></svg>(03) 5598 4731</div>
    <div><svg viewBox="0 0 22 22" fill="none" stroke="#0a2a9c" stroke-width="2"><rect x="3" y="8" width="16" height="10"/><path d="M6 8V3h10v5"/></svg>(03) 5598 4706</div>
    <div><svg viewBox="0 0 22 22" fill="none" stroke="#0a2a9c" stroke-width="2"><rect x="2" y="5" width="18" height="12"/><path d="M2 5l9 7 9-7"/></svg>ross.kedwick@<br>brindelllegal-example.com.au</div>
    <div><svg viewBox="0 0 22 22" fill="#0a2a9c"><path d="M11 1a7 7 0 00-7 7c0 5 7 13 7 13s7-8 7-13a7 7 0 00-7-7zm0 10a3 3 0 110-6 3 3 0 010 6z"/></svg>17 Pellow Road,<br>Hamilton VIC 3300</div>
  </div>
</section>

<footer class="site-footer">
  <div class="social"><span></span><span></span><span></span><span></span></div>
  <div class="copyright">© 2015 Brindell Legal</div>
  <div class="badges"><div class="badge"></div><div class="badge wide"></div><div class="badge wide"></div></div>
</footer>
</body>
</html>
```